terras letterhead

We would like to create a new letterhead that our company will use for proposals, invoices, statements and letters. Our company name is Terra-Vantage. We are a landscape design/build and landscape maintenance company. We have a web site Terra-Vantage.example where our logo (the leaf with the lettering within it only) is displayed.

Industry/Entity Type

Graphic Design

Requirements
Must have
• Address and info on our current letterhead (uploaded)
Nice to have
• We would like the design to look presentable in grey scale as well as color.
Should not have
• Do not want to infringe much on the normal useable area within the normal print areas.

```html
<!DOCTYPE html>
<html lang="en">
<head>
<meta charset="utf-8">
<title>Terra-Vantage Letterhead</title>
<link rel="stylesheet" href="https://fonts.googleapis.com/css2?family=Arimo:wght@400;700&display=swap">
<style>
  :root {
    --backdrop: #e9e6e1;
    --paper: #ffffff;
    --forest: #1f4a24;
    --lime: #7cc43a;
    --ink-light: #ffffff;
  }
  * { margin: 0; padding: 0; box-sizing: border-box; }
  html, body {
    width: 1200px;
    height: 1129px;
    overflow: hidden;
    background: var(--backdrop);
    font-family: "Arimo", Arial, sans-serif;
  }
  .letterhead {
    position: absolute;
    left: 190px;
    top: 34px;
    width: 820px;
    height: 1060px;
    background: var(--paper);
    box-shadow: 0 6px 18px rgba(0,0,0,0.18);
    overflow: hidden;
  }
  .letterhead__bands {
    position: absolute;
    inset: 0;
    width: 100%;
    height: 100%;
  }
  .band-dark { fill: var(--forest); }
  .band-accent { fill: var(--lime); }
  .contact-block {
    position: absolute;
    left: 30px;
    top: 96px;
    color: var(--ink-light);
    font-size: 17px;
    line-height: 22px;
  }
  .brand-name {
    position: absolute;
    right: 44px;
    top: 72px;
    display: flex;
    align-items: center;
    gap: 10px;
    color: var(--forest);
    font-weight: 700;
    font-size: 26px;
    letter-spacing: 1px;
  }
  .brand-name__dot {
    width: 16px;
    height: 16px;
    border-radius: 50%;
    background: var(--forest);
  }
  .footer-url {
    position: absolute;
    left: 30px;
    bottom: 22px;
    color: var(--ink-light);
    font-size: 17px;
  }
</style>
</head>
<body>
  <main class="letterhead">
    <svg class="letterhead__bands" viewBox="0 0 820 1060" preserveAspectRatio="none" aria-hidden="true">
      <!-- header band -->
      <path class="band-accent" d="M0 0 H820 V40 C600 40 520 70 420 140 C330 200 200 218 0 210 Z"/>
      <path class="band-dark" d="M0 0 H820 V30 C600 30 510 58 410 128 C320 190 200 206 0 198 Z"/>
      <!-- footer band -->
      <path class="band-accent" d="M0 1060 V972 C60 940 170 918 300 922 C420 926 520 958 600 968 L820 968 V1060 Z"/>
      <path class="band-dark" d="M0 1060 V984 C60 952 170 932 300 936 C420 940 510 972 600 980 L820 980 V1060 Z"/>
    </svg>

    <address class="contact-block" style="font-style: normal;">
      <div class="contact-block__street">1185 Meadowbrook Lane, Fernhill, NJ 07999</div>
      <div class="contact-block__phones">(555) 013-4472&nbsp; Fax: (555) 013-4490</div>
      <div class="contact-block__email">Service@Terra-Vantage.example</div>
    </address>

    <div class="brand-name">
      <span class="brand-name__dot"></span>
      <span class="brand-name__text">TERRA-VANTAGE</span>
    </div>

    <div class="footer-url">www.terra-vantage.example</div>
  </main>
</body>
</html>
```